Holistic/ Sports Psychologist needs flyer design

I need a flyer designed that catches the attention of potential customers - (parents of young athletes and athletes) who may be looking for psychological services. I have a logo and all the relevant info for the flyer but would like someone to take it and make it look creative, fun, fresh and attention getting for high school and college athletes. The colors used can be from my logo design which represents my holistic approach.
Target Market(s)
high school and collegiate athletes
Industry/Entity Type
sports psychology
Requirements
Must have
- Info I put on the flyer with my logo and please add some graphics and color based on my logo

```html
<!DOCTYPE html>
<html lang="en">
<head>
<meta charset="utf-8">
<title>Holistic Psychology and Sports Psychology Consulting</title>
<link href="https://fonts.googleapis.com/css2?family=Itim&family=Roboto:ital,wght@0,400;0,500;0,700;1,500&display=swap" rel="stylesheet">
<style>
  :root {
    --header-blue: #366aa0;
    --accent-orange: #f2a634;
    --sky-blue: #9ccbe8;
    --paper-top: #dde9f3;
    --paper-bottom: #f7f9fb;
    --leaf-green: #a8d27a;
    --ink: #1f1f1f;
    --ink-soft: #3d4650;
    --icon-blue: #2f5f96;
    --white: #ffffff;
  }
  * { margin: 0; padding: 0; box-sizing: border-box; }
  html, body { width: 942px; height: 1200px; overflow: hidden; }
  body { font-family: "Roboto", Arial, sans-serif; color: var(--ink); }

  .flyer {
    position: relative;
    width: 942px;
    height: 1200px;
    overflow: hidden;
    background: linear-gradient(180deg, var(--paper-top) 0%, var(--paper-bottom) 70%);
  }
  .header-shape { position: absolute; left: 0; top: 0; width: 942px; height: 320px; }

  .title {
    position: absolute;
    top: 48px; left: 0; width: 942px;
    text-align: center;
    font-family: "Itim", "Comic Sans MS", cursive;
    color: var(--white);
    font-size: 58px;
    line-height: 64px;
  }

  .brand {
    position: absolute; left: 52px; top: 246px;
    display: flex; align-items: center; gap: 10px;
  }
  .brand-dot {
    width: 84px; height: 84px; border-radius: 50%;
    background: var(--header-blue);
  }
  .brand-name {
    font-family: "Roboto", Arial, sans-serif;
    font-weight: 500;
    font-size: 21px;
    color: var(--header-blue);
  }
  .brand-bar {
    position: absolute; left: 137px; top: 296px;
    width: 259px; height: 16px; background: var(--leaf-green);
  }

  .bio {
    position: absolute; left: 60px; top: 352px; width: 340px;
    font-size: 15.6px; line-height: 23px; color: var(--ink);
  }
  .bio strong { font-size: 19px; font-weight: 700; }
  .bio p + p { margin-top: 23px; }

  .column-divider {
    position: absolute; left: 438px; top: 263px;
    width: 1px; height: 545px; background: var(--white);
  }

  .ways-heading {
    position: absolute; left: 497px; top: 256px; width: 420px;
    font-style: italic; font-weight: 500;
    font-size: 20.5px; line-height: 28px; color: var(--ink-soft);
  }

  .service {
    position: absolute; left: 495px; width: 420px;
    display: flex; gap: 26px;
  }
  .service-icon { width: 42px; height: 48px; flex: none; margin-top: 2px; }
  .service-text {
    width: 340px; font-size: 15.2px; line-height: 20.3px; color: var(--ink-soft);
  }
  .service-text b { font-weight: 700; font-size: 16px; color: var(--ink-soft); }

  .landscape {
    position: absolute; left: 0; top: 700px; width: 942px; height: 500px;
  }

  .online-panel {
    position: absolute; left: 99px; top: 1150px; width: 295px; height: 217px;
  }
  .online-box {
    position: absolute; left: 99px; top: 983px; width: 295px; height: 217px;
    background: linear-gradient(180deg, rgba(150,110,60,0.35) 0%, rgba(80,80,80,0.55) 100%);
    text-align: center; color: var(--white);
  }
  .online-headline {
    font-family: "Itim", "Comic Sans MS", cursive;
    font-size: 33px; line-height: 35px; margin-top: 4px;
  }
  .contact {
    margin-top: 12px; font-size: 16.2px; line-height: 22px; font-weight: 500;
  }

  .motto {
    position: absolute; right: 49px; top: 1040px;
    text-align: right;
    font-family: "Itim", "Comic Sans MS", cursive;
    font-size: 36px; line-height: 36px; color: var(--ink);
  }
  .motto-bar {
    position: absolute; left: 711px; top: 1162px;
    width: 182px; height: 8px; background: var(--leaf-green);
  }
</style>
</head>
<body>
<main class="flyer">

  <svg class="header-shape" viewBox="0 0 942 320" aria-hidden="true">
    <path d="M0,180 C120,200 260,215 420,205 C600,195 760,205 942,255 L942,320 C900,280 840,250 780,238 C600,210 420,205 0,230 Z" fill="var(--accent-orange)"/>
    <path d="M700,225 C820,235 900,260 942,300 L942,250 Z" fill="var(--sky-blue)"/>
    <path d="M0,0 L942,0 L942,243 C820,215 680,200 520,206 C330,213 160,222 0,180 Z" fill="var(--header-blue)"/>
    <path d="M760,208 C860,220 920,250 942,300 L942,243 C880,226 820,214 760,208 Z" fill="var(--sky-blue)"/>
  </svg>

  <h1 class="title">Holistic Psychology and<br>Sports Psychology Consulting</h1>

  <div class="brand">
    <span class="brand-dot"></span>
    <span class="brand-name">Dr. Elena Hartwell</span>
  </div>
  <div class="brand-bar"></div>

  <section class="bio">
    <p><strong>Dr. Elena Hartwell</strong> is a licensed psychologist. She understands the unique experiences of athletes due to her background as an All-American swimmer, collegiate and age group swim coach, parent of a collegiate/professional athlete, and sports psychology researcher. She works with athletes to optimize performance and overall well-being.</p>
    <p>Her specializations include: performance anxiety, mental performance, stress management, anxiety, depressions, trauma, life transitions, relationship issues, injury, and sleep.</p>
  </section>

  <div class="column-divider"></div>

  <h2 class="ways-heading">Ways to Improve Athletic Performance Using Sports and Holistic Psychology</h2>

  <div class="service" style="top:349px">
    <svg class="service-icon" viewBox="0 0 42 48" aria-hidden="true">
      <path d="M21,2 C9,2 2,10 2,20 C2,27 6,31 8,34 L8,46 L26,46 L26,40 L32,40 C35,40 36,38 36,35 L36,30 L40,28 L36,20 C36,10 31,2 21,2 Z" fill="var(--icon-blue)"/>
      <circle cx="20" cy="18" r="9" fill="none" stroke="var(--white)" stroke-width="2"/>
    </svg>
    <div class="service-text"><b>Mental Skills Training – Ex:</b><br>visualization, goal-setting, motivation, self- talk, mindset, concentration techniques.</div>
  </div>

  <div class="service" style="top:432px">
    <svg class="service-icon" viewBox="0 0 42 48" aria-hidden="true">
      <path d="M12,4 L30,4 L38,12 L38,44 L12,44" fill="none" stroke="var(--icon-blue)" stroke-width="3"/>
      <path d="M30,4 L30,12 L38,12" fill="none" stroke="var(--icon-blue)" stroke-width="3"/>
      <path d="M3,40 L13,28 L20,33 L30,22" fill="none" stroke="var(--icon-blue)" stroke-width="3"/>
      <path d="M24,21 L31,21 L31,28" fill="none" stroke="var(--icon-blue)" stroke-width="3"/>
    </svg>
    <div class="service-text"><b>Performance Enhancement –</b> eliminate psychological barriers that are hindering performance such as self- doubt, perfectionism, fear of failure, and burnout.</div>
  </div>

  <div class="service" style="top:535px">
    <svg class="service-icon" viewBox="0 0 42 48" aria-hidden="true">
      <path d="M21,2 C9,2 2,10 2,20 C2,27 6,31 8,34 L8,46 L26,46 L26,40 L32,40 C35,40 36,38 36,35 L36,30 L40,28 L36,20 C36,10 31,2 21,2 Z" fill="var(--icon-blue)"/>
      <path d="M20,26 L12,18 C10,14 14,10 17,12 L20,15 L23,12 C26,10 30,14 28,18 Z" fill="var(--white)"/>
    </svg>
    <div class="service-text"><b>Mental Health-</b> anxiety and stress management by using things such as relaxation techniques, breathwork, and mindfulness practices.</div>
  </div>

  <div class="service" style="top:637px">
    <svg class="service-icon" viewBox="0 0 42 48" aria-hidden="true">
      <circle cx="21" cy="5" r="4" fill="var(--icon-blue)"/>
      <path d="M15,20 L15,13 C15,10 27,10 27,13 L27,20 Z" fill="var(--icon-blue)"/>
      <circle cx="8" cy="11" r="3.5" fill="var(--icon-blue)"/>
      <path d="M2,24 L2,18 C2,15 14,15 14,18 L14,24 Z" fill="var(--icon-blue)"/>
      <circle cx="34" cy="11" r="3.5" fill="var(--icon-blue)"/>
      <path d="M28,24 L28,18 C28,15 40,15 40,18 L40,24 Z" fill="var(--icon-blue)"/>
      <path d="M21,22 L21,28 M10,27 L16,33 M32,27 L26,33" stroke="var(--icon-blue)" stroke-width="2.5"/>
      <circle cx="21" cy="34" r="3" fill="none" stroke="var(--icon-blue)" stroke-width="2.5"/>
      <rect x="16" y="38" width="10" height="8" rx="2" fill="none" stroke="var(--icon-blue)" stroke-width="2.5"/>
    </svg>
    <div class="service-text"><b>Injury Recovery Support-</b> assist athletes in maintain resilience and positive mental attitude during rehabilitation as well as processing emotions relating to any potential trauma caused by the injury or life transitions resulting from it.</div>
  </div>

  <div class="service" style="top:784px">
    <svg class="service-icon" viewBox="0 0 42 48" aria-hidden="true">
      <path d="M13,5 L29,5 L40,16 L40,32 L29,43 L13,43 L2,32 L2,16 Z" fill="var(--icon-blue)"/>
      <path d="M13,5 L29,5 L40,16 L40,32 L29,43 L13,43 L2,32 L2,16 Z" fill="none" stroke="var(--white)" stroke-width="2" transform="translate(21 24) scale(0.82) translate(-21 -24)"/>
      <path d="M15,18 L27,30 M27,18 L15,30" stroke="var(--white)" stroke-width="4" stroke-linecap="round"/>
    </svg>
    <div class="service-text"><b>Burnout prevention-</b> teach athletes how to have balance in sports and life so they can experience longevity in their sports as well as overall optimal health and well-being.</div>
  </div>

  <svg class="landscape" viewBox="0 0 942 500" role="img" aria-label="Illustration of a rising sun, three pine trees on golden hills and a curling teal ocean wave">
    <defs>
      <linearGradient id="scene-tones" x1="0" y1="0" x2="0" y2="1">
        <stop offset="0" stop-color="#e9b57a"/>
        <stop offset="0.45" stop-color="#dea35f"/>
        <stop offset="0.75" stop-color="#4d8197"/>
        <stop offset="1" stop-color="#275c72"/>
      </linearGradient>
      <linearGradient id="shore-tones" x1="0" y1="0" x2="1" y2="0">
        <stop offset="0" stop-color="#e4a965"/>
        <stop offset="1" stop-color="#f5dcbd"/>
      </linearGradient>
    </defs>
    <path d="M0,130 C150,90 330,100 520,180 C640,230 760,170 942,205 L942,500 L0,500 Z" fill="url(#scene-tones)"/>
    <path d="M600,230 C720,190 850,185 942,200 L942,500 L600,500 Z" fill="url(#shore-tones)"/>
  </svg>

  <div class="online-box">
    <div class="online-headline">All services are<br>provided online</div>
    <div class="contact">
      2280 Harbor Lane #105<br>
      Coral Bay, FL 32190<br>
      904-555-0182<br>
      www.DrElenaHartwell.com
    </div>
  </div>

  <div class="motto">Be You<br>Be Love<br>Be Present</div>
  <div class="motto-bar"></div>

</main>
</body>
</html>
```